Company Broshure Oil&Energy Industry

We have recently completed a company rebranding, and our new website is now fully live and available at www.velmorquist.ro.

To ensure consistency across all communication materials, we would like to redesign our company presentation flyer/brochure so that it fully reflects the updated branding and visual identity of the website.

Please find attached our current brochure (last item uploaded on the list), which should be redesigned in line with the new website’s look and feel. The overall structure and text content should remain unchanged; only the layout and visual design need to be updated. I have uploaded pictures from of the website theme. Can be used by designers for the new design.
Updates

We uploaded pictures belonging to website design theme that can be used for the new brochure.

Target Market(s)

EPC Contractors

Industry/Entity Type

Oil&Energy

Font styles to use
Other font styles liked:
• Calibri

Colors
0094D4
00A9DD
6FCCEA
C7EBF8
E9F6FB

Requirements
Must have
• a clear structure, elegant layout
Nice to have
• I would like to have a dynamic approach. To feel elegant and alive.

```html
<!DOCTYPE html>
<html lang="en">
<head>
<meta charset="utf-8">
<title>Velmorquist Group – Company Presentation</title>
<link href="https://fonts.googleapis.com/css2?family=Roboto:wght@300;400;700;900&family=Lato:wght@400;700&family=Montserrat:wght@400;500&display=swap" rel="stylesheet">
<style>
  :root{
    --stage:#c8c8c8;
    --ink:#222228;
    --navy:#0f3a6b;
    --white:#ffffff;
    --accent:#3ea1db;
    --teal:#2fb5c7;
    --blue-deep:#1a75bc;
    --blue-mid:#3d8fd0;
    --blue-sky:#3aa5dc;
    --cyan-soft:#6ccad9;
    --mint:#7fd0c0;
    --green:#8cc63f;
    --paper-grey:#ebecee;
    --muted:#5a5a5f;
  }
  html,body{margin:0;padding:0;}
  body{
    width:1050px;height:1200px;overflow:hidden;
    background:var(--stage);position:relative;
    font-family:"Lato",Calibri,sans-serif;
  }
  .page{position:absolute;display:block;}
  .cover{left:294px;top:87px;width:465px;height:328px;}
  .spread-who{left:59px;top:438px;width:465px;height:328px;}
  .spread-services{left:528px;top:438px;width:463px;height:328px;}
  .spread-industry{left:59px;top:778px;width:465px;height:328px;}
  .spread-phases{left:528px;top:778px;width:465px;height:328px;}

  .brand-word{font-family:"Roboto",sans-serif;font-weight:400;}
  .cover-title{font-family:"Roboto",sans-serif;font-weight:900;font-size:35px;fill:var(--white);}
  .cover-sub{font-family:"Montserrat",sans-serif;font-size:13px;fill:var(--teal);letter-spacing:.4px;}
  .cover-tag{font-family:"Montserrat",sans-serif;font-size:10px;fill:var(--white);}
  .cover-motto{font-family:"Montserrat",sans-serif;font-size:9.5px;fill:var(--muted);}
  .section-title{font-family:"Roboto",sans-serif;font-weight:400;font-size:25px;fill:var(--accent);}
  .lead{font-family:"Lato",sans-serif;font-size:10.5px;fill:var(--white);}
  .body-copy{font-family:"Lato",sans-serif;font-size:7.6px;fill:var(--white);}
  .pill-label{font-family:"Lato",sans-serif;font-size:11px;fill:var(--white);text-anchor:middle;}
  .pill{fill:none;stroke:var(--white);stroke-width:1;}
  .trail{fill:none;stroke:#cfd3d8;stroke-width:1;stroke-dasharray:1.5 2.5;}
  .footer-mark{font-family:"Roboto",sans-serif;font-weight:400;font-size:28px;fill:var(--white);}
  .badge{fill:#3a85cc;stroke:var(--white);stroke-width:5;}
  .glyph{fill:none;stroke:var(--white);stroke-width:4;stroke-linecap:round;stroke-linejoin:round;}
</style>
</head>
<body>

<svg width="0" height="0" style="position:absolute">
  <defs>
    <linearGradient id="chevron-fade" x1="0" y1="0" x2="520" y2="0" gradientUnits="userSpaceOnUse">
      <stop offset="0" stop-color="#1a75bc"/>
      <stop offset="0.45" stop-color="#2fa5b5"/>
      <stop offset="0.8" stop-color="#8cc63f"/>
    </linearGradient>
    <linearGradient id="cover-band" x1="270" y1="500" x2="794" y2="340" gradientUnits="userSpaceOnUse">
      <stop offset="0" stop-color="#8cc63f"/>
      <stop offset="0.45" stop-color="#3fa8a6"/>
      <stop offset="0.75" stop-color="#1a75bc"/>
    </linearGradient>
    <linearGradient id="tone-stairs" x1="0" y1="0" x2="1" y2="1">
      <stop offset="0" stop-color="#f2f2f3"/>
      <stop offset="0.6" stop-color="#d9dadd"/>
      <stop offset="1" stop-color="#8e8f96"/>
    </linearGradient>
    <linearGradient id="tone-site" x1="0" y1="0" x2="1" y2="1">
      <stop offset="0" stop-color="#c7d3dc"/>
      <stop offset="0.5" stop-color="#b88a5c"/>
      <stop offset="1" stop-color="#c9d86a"/>
    </linearGradient>
    <linearGradient id="tone-refinery" x1="0" y1="0" x2="1" y2="1">
      <stop offset="0" stop-color="#9aa7b4"/>
      <stop offset="0.6" stop-color="#c6cbd1"/>
      <stop offset="1" stop-color="#d98a7a"/>
    </linearGradient>
    <linearGradient id="tone-windfarm" x1="0" y1="0" x2="0" y2="1">
      <stop offset="0" stop-color="#8b8e97"/>
      <stop offset="0.55" stop-color="#a89579"/>
      <stop offset="1" stop-color="#6b5a45"/>
    </linearGradient>
    <linearGradient id="tone-crew" x1="0" y1="0" x2="1" y2="0">
      <stop offset="0" stop-color="#3a3d45"/>
      <stop offset="0.5" stop-color="#b0404a"/>
      <stop offset="1" stop-color="#c9c4c2"/>
    </linearGradient>
  </defs>
</svg>

<!-- Cover -->
<svg class="page cover" viewBox="0 0 794 560" aria-label="Company presentation cover">
  <rect width="794" height="560" fill="var(--white)"/>
  <g role="img" aria-label="Photo of three workers in high-visibility gear climbing a white staircase on a storage tank">
    <polygon points="520,0 794,0 794,310 540,385 345,205" fill="url(#tone-stairs)"/>
  </g>
  <polygon points="0,115 440,365 110,560 0,560" fill="var(--ink)"/>
  <polygon points="165,205 255,155 255,255" fill="var(--blue-deep)"/>
  <polygon points="255,155 345,205 255,255" fill="var(--blue-mid)"/>
  <polygon points="255,255 345,205 345,310" fill="var(--blue-sky)"/>
  <polygon points="345,205 440,260 345,310" fill="var(--cyan-soft)"/>
  <polygon points="345,310 440,260 440,365" fill="var(--mint)"/>
  <polygon points="440,260 530,315 440,365" fill="#9ad6b4"/>
  <polygon points="330,445 445,375 445,512" fill="var(--paper-grey)"/>
  <polygon points="445,375 610,470 445,512" fill="#f3f3f4"/>
  <polygon points="270,465 445,512 794,312 794,378 475,560 385,560" fill="url(#cover-band)"/>
  <text class="brand-word" x="82" y="112" font-size="58" fill="var(--navy)">VMG</text>
  <text class="cover-title" x="53" y="290">VELMORQUIST</text>
  <text class="cover-title" x="53" y="330">GROUP</text>
  <line x1="55" y1="380" x2="332" y2="380" stroke="var(--teal)" stroke-width="1.2"/>
  <text class="cover-sub" x="55" y="407">COMPANY PRESENTATION</text>
  <text class="cover-tag" x="58" y="448">Your Valuable Partner for</text>
  <text class="cover-tag" x="58" y="460">Oil &amp;Energy Projects</text>
  <text class="cover-motto" x="644" y="516">Different. Better. Reliable.</text>
  <text class="cover-motto" x="644" y="529">Since 2003</text>
</svg>

<!-- Who we are -->
<svg class="page spread-who" viewBox="0 0 794 560" aria-label="Who we are">
  <rect width="794" height="560" fill="var(--ink)"/>
  <g role="img" aria-label="Photo of a worker in an orange hard hat looking at scaffolding">
    <polygon points="47,0 794,0 794,165 520,330 340,218 47,310" fill="url(#tone-site)"/>
  </g>
  <polygon points="0,20 340,218 40,335 0,335" fill="var(--ink)"/>
  <polygon points="47,97 245,215 47,310" fill="#c4ccd2"/>
  <polygon points="0,390 340,218 520,330 455,372 335,300 0,487" fill="url(#chevron-fade)"/>
  <polygon points="335,300 450,365 335,430 220,365" fill="#2c3a4c" opacity=".8"/>
  <polygon points="450,365 565,435 450,505 335,435" fill="#334150" opacity=".7"/>
  <polygon points="565,435 680,505 565,560 450,505" fill="#3b4650" opacity=".7"/>
  <circle class="badge" cx="130" cy="418" r="48"/>
  <circle cx="130" cy="400" r="4" fill="var(--white)"/>
  <path class="glyph" d="M124 412 H132 V438 M124 438 H138"/>
  <text class="footer-mark" x="67" y="530">VMG</text>
  <text class="section-title" x="608" y="328">WHO</text>
  <text class="section-title" x="608" y="361">WE ARE</text>
  <text class="lead" x="610" y="382">Velmorquist Group is a</text>
  <text class="lead" x="610" y="396">Romanian registred company,</text>
  <text class="lead" x="610" y="410">founded in 2003.</text>
  <g class="body-copy">
    <text x="225" y="388">We have been active in Oil&amp;Energy industry serving local</text>
    <text x="225" y="398">and international market by sourcing highly specilised</text>
    <text x="225" y="408">professionals for Oil&amp;Energy projects.</text>
    <text x="225" y="428">We offer a wide range of services that encompass every</text>
    <text x="225" y="438">stage of the process, starting from the initial selection of</text>
    <text x="225" y="448">professionals and extending to the management of employ-</text>
    <text x="225" y="458">ment and logistics (mobilisation) for the assigned resources.</text>
    <text x="225" y="468">Whether the project is located domestically or</text>
    <text x="225" y="492">We have been active in Oil&amp;Energy industry serving local</text>
    <text x="225" y="502">and international market by sourcing highly specilised</text>
    <text x="225" y="512">professionals for Oil&amp;Energy projects.</text>
  </g>
</svg>

<!-- Services -->
<svg class="page spread-services" viewBox="0 0 790 560" aria-label="Services">
  <rect width="790" height="560" fill="var(--ink)"/>
  <g transform="translate(790,0) scale(-1,1)">
    <g role="img" aria-label="Photo of an engineer in a white hard hat reading plans in front of a refinery">
      <polygon points="0,0 790,0 790,310 520,330 340,218 0,165" fill="url(#tone-refinery)"/>
    </g>
    <polygon points="0,20 340,218 40,335 0,335" fill="var(--ink)"/>
    <polygon points="37,97 245,215 37,310" fill="#c8ccd0"/>
    <polygon points="0,390 340,218 520,330 455,372 335,300 0,487" fill="url(#chevron-fade)"/>
    <polygon points="335,300 450,365 335,430 220,365" fill="#2c3a4c" opacity=".8"/>
    <polygon points="450,365 565,435 450,505 335,435" fill="#334150" opacity=".7"/>
    <polygon points="565,435 680,505 565,560 450,505" fill="#3b4650" opacity=".7"/>
  </g>
  <circle class="badge" cx="660" cy="418" r="48"/>
  <circle class="glyph" cx="660" cy="418" r="17" stroke-dasharray="6 3.5" stroke-width="7"/>
  <path class="glyph" d="M653 432 V418 M667 432 V418 M653 412 L660 404 L667 412"/>
  <text class="footer-mark" x="693" y="530">VMG</text>
  <text class="section-title" x="67" y="328">SERVICES</text>
  <text class="lead" x="69" y="350">Velmorquist Group is a</text>
  <text class="lead" x="69" y="364">Romanian registred company,</text>
  <text class="lead" x="69" y="378">founded in 2003.</text>
  <g class="body-copy">
    <text x="67" y="412">We have been active in Oil&amp;Energy industry serving local</text>
    <text x="67" y="422">and international market by sourcing highly specilised</text>
    <text x="67" y="432">professionals for Oil&amp;Energy projects.</text>
    <text x="67" y="458">We offer a wide range of services that encompass every</text>
    <text x="67" y="468">stage of the process, starting from the initial selection of</text>
    <text x="67" y="478">professionals and extending to the management of employ-</text>
    <text x="67" y="488">ment and logistics (mobilisation) for the assigned resources.</text>
    <text x="67" y="498">Whether the project is located domestically or</text>
  </g>
  <text class="lead" x="441" y="488">Velmorquist Group is a</text>
  <text class="lead" x="441" y="502">Romanian registred company,</text>
  <text class="lead" x="441" y="516">founded in 2003.</text>
</svg>

<!-- Industry we serve -->
<svg class="page spread-industry" viewBox="0 0 794 560" aria-label="Industry we serve">
  <rect width="794" height="560" fill="var(--ink)"/>
  <g role="img" aria-label="Photo of two engineers in hard hats looking over a wind farm at dusk">
    <polygon points="0,0 794,0 794,165 520,330 340,218 47,310 0,20" fill="url(#tone-windfarm)"/>
  </g>
  <polygon points="0,20 340,218 40,335 0,335" fill="var(--ink)"/>
  <polygon points="37,97 245,215 37,325" fill="#5b5650"/>
  <polygon points="0,390 340,218 520,330 455,372 335,300 0,487" fill="url(#chevron-fade)"/>
  <circle class="badge" cx="130" cy="418" r="48"/>
  <circle class="glyph" cx="130" cy="418" r="20" stroke-dasharray="6 3.5" stroke-width="7"/>
  <path class="glyph" d="M118 420 L126 413 L134 420 L142 413" stroke-width="3"/>
  <text class="footer-mark" x="45" y="530">VMG</text>
  <path class="trail" d="M330 352 C345 335 370 335 373 365"/>
  <path class="trail" d="M385 397 C400 380 430 380 436 410"/>
  <path class="trail" d="M440 440 C455 425 490 425 495 478"/>
  <rect class="pill" x="237" y="357" width="116" height="38" rx="4"/>
  <text class="pill-label" x="295" y="380">OIL&amp;GAS</text>
  <rect class="pill" x="288" y="397" width="113" height="38" rx="4"/>
  <text class="pill-label" x="344" y="420">POWER</text>
  <rect class="pill" x="350" y="441" width="103" height="38" rx="4"/>
  <text class="pill-label" x="401" y="464" font-size="8.5">PETROCHEMISTRY</text>
  <rect class="pill" x="407" y="485" width="108" height="38" rx="4"/>
  <text class="pill-label" x="461" y="508">PHARMA</text>
  <text class="section-title" x="608" y="328">INDUSTRY</text>
  <text class="section-title" x="608" y="361">WE SERVE</text>
  <text class="lead" x="610" y="382">Velmorquist Group is a</text>
  <text class="lead" x="610" y="396">Romanian registred company,</text>
  <text class="lead" x="610" y="410">founded in 2003.</text>
  <g class="body-copy">
    <text x="542" y="443">We have been active in Oil&amp;Energy industry serving local</text>
    <text x="542" y="453">and international market by sourcing highly specilised</text>
    <text x="542" y="463">professionals for Oil&amp;Energy projects.</text>
    <text x="542" y="484">We offer a wide range of services that encompass every</text>
    <text x="542" y="494">stage of the process, starting from the initial selection of</text>
    <text x="542" y="504">professionals and extending to the management of employ-</text>
    <text x="542" y="514">ment and logistics (mobilisation) for the assigned resources.</text>
    <text x="542" y="524">Whether the project is located domestically or</text>
  </g>
</svg>

<!-- Project phases -->
<svg class="page spread-phases" viewBox="0 0 794 560" aria-label="Project phases we cover">
  <rect width="794" height="560" fill="var(--ink)"/>
  <g transform="translate(794,0) scale(-1,1)">
    <g role="img" aria-label="Photo of engineers in white hard hats and red coveralls on site">
      <polygon points="0,0 794,0 794,310 520,330 340,218 0,165" fill="url(#tone-crew)"/>
    </g>
    <polygon points="0,20 340,218 40,335 0,335" fill="var(--ink)"/>
    <polygon points="37,97 245,215 37,325" fill="#b8aaa6"/>
    <polygon points="0,390 340,218 520,330 455,372 335,300 0,487" fill="url(#chevron-fade)"/>
  </g>
  <circle class="badge" cx="663" cy="418" r="48"/>
  <circle class="glyph" cx="663" cy="418" r="22" stroke-dasharray="6 3.5" stroke-width="5"/>
  <circle class="glyph" cx="663" cy="418" r="12" stroke-width="3"/>
  <path class="glyph" d="M657 418 L661 422 L669 413" stroke-width="3"/>
  <text class="footer-mark" x="711" y="530">VMG</text>
  <path class="trail" d="M140 257 C160 245 175 255 175 290"/>
  <path class="trail" d="M185 300 C205 285 225 295 228 335"/>
  <path class="trail" d="M240 345 C260 330 280 340 285 375"/>
  <path class="trail" d="M295 385 C315 375 335 385 345 425"/>
  <path class="trail" d="M345 435 C365 425 395 435 400 475"/>
  <rect class="pill" x="45" y="261" width="112" height="37" rx="4"/>
  <text class="pill-label" x="101" y="284">Engineering</text>
  <rect class="pill" x="95" y="306" width="110" height="37" rx="4"/>
  <text class="pill-label" x="150" y="329">Construction</text>
  <rect class="pill" x="155" y="349" width="98" height="37" rx="4"/>
  <text class="pill-label" x="204" y="372">Commissioning</text>
  <rect class="pill" x="205" y="391" width="105" height="40" rx="4"/>
  <text class="pill-label" x="257" y="409">Start-up &amp;</text>
  <text class="pill-label" x="257" y="423">Operation</text>
  <rect class="pill" x="272" y="441" width="88" height="38" rx="4"/>
  <text class="pill-label" x="316" y="464">Maintenance</text>
  <rect class="pill" x="323" y="485" width="116" height="38" rx="4"/>
  <text class="pill-label" x="381" y="508">Operation</text>
  <g class="body-copy">
    <text x="350" y="384">VMG is able to assit you along project life time by offering</text>
    <text x="350" y="394">the key resources needed</text>
    <text x="350" y="404">to complete and run the project.</text>
  </g>
  <text class="section-title" x="35" y="458">PROJECT</text>
  <text class="section-title" x="35" y="491">PHASES WE COVER</text>
  <text class="lead" x="467" y="499">Velmorquist Group is a</text>
  <text class="lead" x="467" y="513">Romanian registred company,</text>
  <text class="lead" x="467" y="527">founded in 2003.</text>
</svg>

</body>
</html>
```